Design the 21st Pacific Lantern Screen Gathering Poster. Think modern, chic, cool, film, movies - driving people to the film festival - the film festivla is in San Francisco and the SF East Bay. Our logo is attached. Dates will be determined soon . please use - November 2 - 11, 2018 (for placement) Keep in mind abstract, chic, modern - eye catching. website is www.plsgfest.org

Target Market(s)

25 - 45 year old - upper middle class

Industry/Entity Type

Film Production

Colors

Designer to choose colors to be used in the design.

Requirements
Must have
• logo (attached) www.plsgfest.org - chic modern design
Nice to have
• best coolest poster ever!
Should not have
• CLIP ART!!!

```html
<!DOCTYPE html>
<html lang="en">
<head>
<meta charset="utf-8">
<title>21st Pacific Lantern Screen Gathering — Poster</title>
<link rel="stylesheet" href="https://fonts.googleapis.com/css2?family=Montserrat:wght@300;400;500&display=swap">
<style>
  :root {
    --page: #ffffff;
    --frame-line: #2a2a2a;
    --red: #f40f0b;
    --red-deep: #e81a12;
    --orange: #ee5a2c;
    --peach: #f6a27a;
    --white: #ffffff;
    --mark: #3aa63a;
  }
  * { margin: 0; padding: 0; box-sizing: border-box; }
  html, body {
    width: 1200px; height: 806px; overflow: hidden;
    background: var(--page);
    font-family: "Montserrat", sans-serif;
  }
  .poster-frame {
    position: absolute; left: 307px; top: 3px;
    width: 586px; height: 800px;
    border: 1.5px solid var(--frame-line);
    background: var(--white);
  }
  .poster {
    position: absolute; left: 13px; top: 13px;
    width: 557px; height: 771px;
    overflow: hidden;
    background: linear-gradient(100deg, var(--red) 0%, var(--red-deep) 45%, var(--orange) 100%);
    color: var(--white);
  }
  .bridge-photo {
    position: absolute; left: 320px; top: 0; width: 237px; height: 771px;
    background: linear-gradient(180deg, rgba(246,162,122,0.30) 0%, rgba(246,162,122,0.70) 55%, rgba(238,90,44,0.35) 100%);
  }
  .guide-line {
    position: absolute; left: 0; top: 0; width: 557px; height: 771px;
  }
  .line {
    position: absolute; white-space: nowrap; line-height: 1;
    transform-origin: left top;
  }
  .brand-dot {
    position: absolute; left: 73px; top: 36px;
    width: 38px; height: 38px; border-radius: 50%;
    background: var(--mark);
  }
  .brand-name {
    left: 17px; top: 79px; font-size: 52px; font-weight: 500; letter-spacing: 4px;
    transform: rotate(-6deg);
  }
  .brand-presents {
    left: 20px; top: 133px; font-size: 18px; font-weight: 400; letter-spacing: 0.5px;
    transform: rotate(-6deg);
  }
  .edition-number {
    left: 55px; top: 337px; font-size: 165px; font-weight: 300;
  }
  .edition-suffix {
    left: 165px; top: 328px; font-size: 160px; font-weight: 300; letter-spacing: -4px;
  }
  .name-small {
    font-size: 38px; font-weight: 400; letter-spacing: 0.5px;
    transform: rotate(-7deg);
  }
  .name-small.first { left: 172px; top: 477px; }
  .name-small.second { left: 175px; top: 515px; }
  .name-large {
    font-weight: 500; transform: rotate(-9deg);
  }
  .name-large.first { left: 77px; top: 567px; font-size: 88px; }
  .name-large.second { left: 86px; top: 641px; font-size: 68px; transform: rotate(-10deg); }
  .dates {
    left: 95px; top: 711px; font-size: 28px; font-weight: 400; letter-spacing: 0.5px;
    transform: rotate(-10deg);
  }
  .website {
    position: absolute; left: 0; right: 0; top: 741px;
    text-align: center; font-weight: 500; font-size: 17px; letter-spacing: 0.5px; line-height: 1;
  }
</style>
</head>
<body>
  <div class="poster-frame">
    <div class="poster">
      <div class="bridge-photo" role="img" aria-label="Photograph of a suspension bridge tower rising through fog, tinted in warm orange"></div>
      <svg class="guide-line" viewBox="0 0 557 771" aria-hidden="true">
        <line x1="86" y1="0" x2="90" y2="32" stroke="#ffffff" stroke-width="8"/>
        <line x1="106" y1="158" x2="132" y2="332" stroke="#ffffff" stroke-width="8"/>
        <line x1="143" y1="352" x2="160" y2="545" stroke="#ffffff" stroke-width="8"/>
      </svg>

      <span class="brand-dot"></span>
      <div class="line brand-name">PLSG</div>
      <div class="line brand-presents">PRESENTS</div>

      <div class="line edition-number">2</div>
      <div class="line edition-suffix">st</div>
      <div class="line name-small first">PACIFIC</div>
      <div class="line name-small second">LANTERN</div>
      <div class="line name-large first">SCREEN</div>
      <div class="line name-large second">GATHERING</div>
      <div class="line dates">NOVEMBER 2 – 11, 2018</div>

      <div class="website">WWW.PLSGFEST.ORG</div>
    </div>
  </div>
</body>
</html>
```